Postcard design to acquire new clients for my Property Management Company

I'm looking for a postcard design that I can send to prospective clients detailing information about my company and services.
Postcard should be eye catching and contain information from www.brightkeyrentals-example.com. I've provided a few screen shots for the most important information and my logo.
Target Market(s)
Real Estate
Industry/Entity Type
Real Estate
Font styles to use
Sans Serif
Requirements
Must have
- Must be eye catching!! this will be a direct mail piece - I'd like for the card to be read and not tossed in the trash immediately.
Design que from the logo.
A place to write / print the receipts name and address.
our physical address - 2287 Marble Lane, Lubbock, TX 79555.
Should not have
- the contact information on the business card is not accurate - please use info from website.

```html
<!DOCTYPE html>
<html lang="en">
<head>
<meta charset="utf-8">
<title>BrightKey Rentals – Postcard</title>
<link href="https://fonts.googleapis.com/css2?family=Montserrat:ital,wght@0,400;0,500;0,600;0,700;0,800;1,500;1,600&display=swap" rel="stylesheet">
<style>
  :root{
    --blue:#0f4f92;
    --blue-deep:#0b3f78;
    --blue-light:#2a6db5;
    --red:#a90f26;
    --red-deep:#780817;
    --grey:#a9abae;
    --grey-icon:#b9bcc0;
    --ink:#1d2b3a;
    --paper:#ffffff;
    --backdrop:#9c9d9f;
  }
  *{box-sizing:border-box;margin:0;padding:0}
  html,body{width:1200px;height:1200px;overflow:hidden}
  body{background:var(--backdrop);font-family:"Montserrat",Arial,sans-serif;color:var(--ink)}
  .stage{position:absolute;left:0;top:0;width:1100px;height:1100px;transform:scale(1.090909);transform-origin:0 0}
  .postcard{position:absolute;left:124px;width:868px;overflow:hidden;background:var(--paper);box-shadow:0 4px 10px rgba(0,0,0,.25)}
  .postcard-front{top:62px;height:473px}
  .postcard-back{top:569px;height:471px}
  .postcard svg.shapes{position:absolute;left:0;top:0}
  .abs{position:absolute}
  .globe{flex:none}

  /* front */
  .brand-name{left:0;top:20px;width:868px;text-align:center;font-size:37px;font-weight:600;letter-spacing:4px;color:var(--blue);white-space:nowrap}
  .housing-badge{left:732px;top:24px;width:58px;height:58px;border-radius:50%;background:#e3e4e6;border:3px solid #fff;box-shadow:0 1px 4px rgba(0,0,0,.3)}
  .offer-text{left:0;top:72px;width:212px;text-align:center;color:#fff;font-size:14.5px;font-weight:500;line-height:19px}
  .offer-text strong{display:block;font-size:18px;font-weight:600;margin-top:2px}
  .region-text{left:650px;top:98px;width:218px;text-align:center;color:#fff;font-size:14px;font-weight:500;line-height:15.5px}
  .headline{left:225px;top:100px;width:420px;text-align:center;color:#fff}
  .headline .big{display:block;font-size:57px;font-weight:600;line-height:60px;letter-spacing:1px}
  .headline .sub{display:block;font-size:21px;font-weight:500;line-height:22px}
  .support{left:230px;top:194px;width:410px;text-align:center;color:var(--blue);font-size:16px;font-weight:700;line-height:20px}
  .service{color:#fff;font-size:18.5px;font-weight:700;line-height:19px}
  .service.left{left:80px;width:200px;text-align:left}
  .service.right{left:580px;width:208px;text-align:right}
  .web-front{left:282px;top:430px;width:290px;height:32px;display:flex;align-items:center;justify-content:center;gap:5px;color:var(--blue);font-size:11.5px;font-weight:600;white-space:nowrap}

  /* back */
  .contact-label{left:0;top:14px;width:190px;text-align:center;color:#fff;font-size:15px;font-weight:600}
  .contact-line{left:205px;top:13px;display:flex;align-items:center;gap:5px;color:var(--blue);font-size:14.5px;font-weight:700;white-space:nowrap}
  .contact-line .dot{display:inline-block;width:19px;height:19px;border-radius:50%;background:var(--blue)}
  .contact-line .email{font-size:12.5px}
  .brand-back{left:606px;top:30px;width:262px;text-align:center;color:var(--blue);font-size:20px;font-weight:600;letter-spacing:3px;line-height:24px}
  .priority-title{left:74px;top:58px;color:#fff;font-size:16.5px;font-weight:700}
  .priority-quote{left:74px;top:78px;width:500px;color:#fff;font-size:9.6px;font-style:italic;font-weight:500;line-height:13px}
  .priority-quote b{font-style:normal;font-weight:700}
  .plan{position:absolute;background:#fff;border-radius:6px;box-shadow:0 1px 6px rgba(0,0,0,.25);overflow:hidden}
  .plan-head{text-align:center;color:#fff;background:var(--grey);padding-top:5px}
  .plan-head h3{font-size:13.5px;font-weight:700;line-height:15px}
  .plan-head p{font-size:10px;font-weight:500;line-height:13px}
  .plan.featured .plan-head{background:var(--blue);padding-top:4px}
  .plan.featured .plan-head h3{font-size:14.5px}
  .price{margin:6px auto 0;width:126px;border:1px solid var(--blue);text-align:center;color:var(--blue);padding:2px 0 1px}
  .price b{display:block;font-size:16px;font-weight:700;line-height:17px}
  .price span{font-size:10px;font-weight:500;line-height:12px}
  .plan ul{list-style:none;margin:10px 0 0 8px;font-size:10.5px;line-height:13px;font-weight:500;color:var(--ink)}
  .plan li{padding-left:9px;position:relative}
  .plan li::before{content:"✓";position:absolute;left:0;top:0;color:var(--blue);font-size:9px}
  .plan li b{font-weight:700}
  .plan li b.plus::after{content:" +";color:var(--blue)}
  .plan.featured ul{margin-top:6px;line-height:12.4px}
  .stars{left:164px;top:142px;width:148px;text-align:center;color:var(--blue);font-size:9px;letter-spacing:2px}
  .web-back{left:650px;top:431px;width:218px;height:30px;display:flex;align-items:center;justify-content:center;gap:5px;color:#fff;font-size:12.5px;font-weight:500;white-space:nowrap}
  .mailing-area{left:650px;top:160px;width:200px;height:250px}
</style>
</head>
<body>
<div class="stage">

  <!-- front side -->
  <section class="postcard postcard-front">
    <svg class="shapes" width="868" height="473" viewBox="0 0 868 473">
      <defs>
        <linearGradient id="blueField" x1="0" y1="0" x2="1" y2="1">
          <stop offset="0" stop-color="#0b3f78"/><stop offset=".5" stop-color="#1a5ea8"/><stop offset="1" stop-color="#0b3f78"/>
        </linearGradient>
        <linearGradient id="redBand" x1="0" y1="0" x2="1" y2="0">
          <stop offset="0" stop-color="#a90f26"/><stop offset="1" stop-color="#7e0918"/>
        </linearGradient>
        <linearGradient id="photoTone" x1="0" y1="0" x2="1" y2="1">
          <stop offset="0" stop-color="#c9d6e6"/><stop offset=".45" stop-color="#e8eef5"/><stop offset=".75" stop-color="#e2b89a"/><stop offset="1" stop-color="#b98a6a"/>
        </linearGradient>
      </defs>
      <rect width="868" height="473" fill="#fff"/>
      <polygon points="0,160 868,160 868,462 0,462" fill="url(#blueField)"/>
      <rect y="462" width="868" height="11" fill="#a9abae"/>
      <polygon points="185,160 690,160 568,462 300,462" fill="#fff"/>
      <polygon points="240,236 630,236 568,462 300,462" fill="url(#photoTone)" role="img" aria-label="Photo of a laptop beside a small model house on a desk"/>
      <polygon points="282,430 572,430 562,462 292,462" fill="#fff"/>
      <polygon points="0,62 198,62 242,160 0,160" fill="url(#redBand)"/>
      <polygon points="612,55 868,55 868,160 642,160" fill="url(#redBand)"/>
      <polygon points="211,188 245,188 228,196" fill="#5a0611"/>
      <polygon points="625,188 650,188 640,196" fill="#5a0611"/>
      <polygon points="226,98 646,98 625,188 245,188" fill="url(#redBand)"/>
      <g fill="#b9bcc0">
        <polygon points="40,180 73,233 7,233"/><polygon points="40,240 73,293 7,293"/>
        <polygon points="40,298 73,351 7,351"/><polygon points="40,358 73,411 7,411"/>
        <polygon points="828,182 861,235 795,235"/><polygon points="828,240 861,293 795,293"/>
        <polygon points="828,298 861,351 795,351"/><polygon points="828,356 861,409 795,409"/>
      </g>
      <g fill="none" stroke="#fff" stroke-width="2">
        <circle cx="40" cy="215" r="5"/><path d="M31 225q9-9 18 0"/>
        <circle cx="40" cy="272" r="7"/><path d="M30 285h20"/>
        <circle cx="38" cy="330" r="6"/><path d="M42 335l6 6"/>
        <path d="M31 394l9-8 9 8v8h-18z"/>
        <path d="M820 220h16M828 208v14M820 214l-4 6h8zM836 214l-4 6h8z"/>
        <path d="M818 285v-8M825 285v-12M832 285v-16M839 285v-6"/>
        <path d="M828 322l8 3v6q0 6-8 9q-8-3-8-9v-6z"/>
        <path d="M819 383l18 18M837 383l-18 18"/>
      </g>
    </svg>

    <div class="abs brand-name">BRIGHTKEY RENTALS</div>
    <div class="abs housing-badge" role="img" aria-label="Fair housing badge"></div>
    <div class="abs offer-text">We offer<br>FULL-SERVICE<br>property management<strong>SOLUTIONS</strong></div>
    <div class="abs region-text">PROPERTY<br>MANAGEMENT<br>ACROSS LUBBOCK, TX</div>
    <div class="abs headline"><span class="big">MAXIMIZE</span><span class="sub">YOUR FINANCIAL RETURNS</span></div>
    <div class="abs support">WITH SUPPORT<br>FROM OUR RENTAL SPECIALISTS</div>

    <div class="abs service left" style="top:196px">TENANT<br>SCREENING</div>
    <div class="abs service left" style="top:254px">RENT<br>COLLECTION</div>
    <div class="abs service left" style="top:315px">PROPERTY<br>INSPECTIONS</div>
    <div class="abs service left" style="top:377px">PROPERTY<br>MARKETING</div>

    <div class="abs service right" style="top:196px">LEGAL<br>GUIDANCE</div>
    <div class="abs service right" style="top:254px">FINANCIAL<br>REPORTING</div>
    <div class="abs service right" style="top:334px">EVICTIONS</div>
    <div class="abs service right" style="top:390px">MAINTENANCE</div>

    <div class="abs web-front">
      <svg class="globe" width="15" height="15" viewBox="0 0 15 15" fill="none" stroke="#0f4f92" stroke-width="1.3"><circle cx="7.5" cy="7.5" r="6.5"/><path d="M1 7.5h13M7.5 1q-4 6.5 0 13q4-6.5 0-13"/></svg>
      <span>BRIGHTKEYRENTALS-EXAMPLE.COM</span>
    </div>
  </section>

  <!-- back side -->
  <section class="postcard postcard-back">
    <svg class="shapes" width="868" height="471" viewBox="0 0 868 471">
      <defs>
        <linearGradient id="backField" x1="0" y1="0" x2="0" y2="1">
          <stop offset="0" stop-color="#ffffff"/><stop offset=".55" stop-color="#e9eef5"/><stop offset=".8" stop-color="#6f93c0"/><stop offset="1" stop-color="#0f4f92"/>
        </linearGradient>
        <linearGradient id="redBack" x1="0" y1="0" x2="1" y2="0">
          <stop offset="0" stop-color="#a90f26"/><stop offset="1" stop-color="#7e0918"/>
        </linearGradient>
      </defs>
      <rect width="868" height="471" fill="url(#backField)"/>
      <polygon points="600,0 868,0 868,461 462,461 632,131 600,131" fill="#fff"/>
      <polygon points="0,8 200,8 186,46 0,46" fill="#a9abae"/>
      <polygon points="200,8 606,8 592,46 186,46" fill="#fff"/>
      <polygon points="0,45 598,45 632,131 0,131" fill="url(#redBack)"/>
      <polygon points="598,45 632,131 598,131" fill="#0f4f92" opacity=".9"/>
      <polygon points="655,431 868,431 868,461 640,461" fill="#0f4f92"/>
      <polygon points="646,431 651,431 636,461 631,461" fill="#0f4f92"/>
      <rect y="461" width="868" height="10" fill="#a9abae"/>
      <g fill="none" stroke="#fff" stroke-width="2.2" stroke-linejoin="round">
        <path d="M18 88h8v24h-8z"/>
        <path d="M26 90l10-4 4-14q3-4 6 0l-1 12h10q5 1 4 6l-3 16q-1 5-6 5H26"/>
        <path d="M42 56v6M50 60l-4 4M34 60l4 4"/>
      </g>
    </svg>

    <div class="abs contact-label">CONTACT OUR TEAM</div>
    <div class="abs contact-line">
      <span class="dot"></span><span>(806) 555-0142</span>
      <span class="dot"></span><span class="email">info@brightkeyrentals-example.com</span>
      <span class="dot"></span>
    </div>
    <div class="abs brand-back">BRIGHTKEY<br>RENTALS</div>

    <div class="abs priority-title">YOUR SATISFACTION IS OUR PRIORITY</div>
    <p class="abs priority-quote">"Dana has been very understanding and willing to work with us on anything that has came up. We moved here from San Antonio, and they were there when we needed our keys on the weekend. Any questions I've had, Dana has been there to help me with it." <b>-Alyssa R.</b></p>

    <div class="abs stars">★★★★★</div>

    <article class="plan" style="left:18px;top:168px;width:146px;height:261px">
      <div class="plan-head" style="height:35px"><h3>LEASE ONLY</h3><p>- You Just Need Tenants -</p></div>
      <div class="price"><b>9%</b><span>of Annual Lease</span></div>
      <ul>
        <li>Professional<br>Photography</li>
        <li>Marketing &amp;<br>Advertising</li>
        <li>Property Showings</li>
        <li>Tenant Screening &amp;<br>Qualifications</li>
        <li>Lease Execution</li>
        <li>Move In Coordination</li>
      </ul>
    </article>

    <article class="plan featured" style="left:164px;top:154px;width:148px;height:292px;z-index:2">
      <div class="plan-head" style="height:40px"><h3>FULL SERVICE</h3><p>- Our Most Popular -</p></div>
      <div class="price" style="margin-top:5px"><b>10%</b><span>of Annual Lease</span></div>
      <ul>
        <li><b>Includes<br><b class="plus">Leasing Service</b></b></li>
        <li>24/7 Emergency<br>Response</li>
        <li>Move In &amp; Out<br>Inspections</li>
        <li>Professional Lease<br>Enforcement</li>
        <li>Schedule &amp; Oversee<br>all Repairs</li>
        <li>Pay all Invoices</li>
        <li>Monthly &amp; Year End<br>Statements</li>
        <li>Annual Market Rent<br>Analysis</li>
      </ul>
    </article>

    <article class="plan" style="left:312px;top:168px;width:146px;height:261px">
      <div class="plan-head" style="height:35px"><h3>PREMIUM SERVICE</h3><p>- Our Premier Service -</p></div>
      <div class="price"><b>12%</b><span>of Annual Lease</span></div>
      <ul>
        <li><b>Includes<br><b class="plus">Full Service Features</b></b></li>
        <li>Professional<br>Video Marketing</li>
        <li>Home Warranty<br>Coordination</li>
        <li>Tenant Retention<br>Program</li>
      </ul>
    </article>

    <div class="abs mailing-area" aria-label="Space for recipient name and address"></div>
    <div class="abs web-back">
      <svg class="globe" width="15" height="15" viewBox="0 0 15 15" fill="none" stroke="#fff" stroke-width="1.3"><circle cx="7.5" cy="7.5" r="6.5"/><path d="M1 7.5h13M7.5 1q-4 6.5 0 13q4-6.5 0-13"/></svg>
      <span>brightkeyrentals-example.com</span>
    </div>
  </section>

</div>
</body>
</html>
```